FUN Sizing Chart for Apparel Company.

We are a company called GROAN, we make cycling jerseys for the fun lovers and beer enthusiasts.....they might even like to bike. www.groankitvale.com We need a nice looking, but more importantly fun sizing chart created that reflects our personality. I've attached the sizing provided by the manufacturer with some information omitted --- what they provided was overkill and confusing, we just need chest measurements. Please create the graphic so that we can somewhat easily adjust the measurements should our pattern change.

FUN is the big winner. Our brand represents light-heartedness. For example, we chose to size our jerseys in volumes of beer which may or may not be incorporated into the graphic:
X-Small = The Half-Pint
Small = The Pint
Medium = The Bomber
Large = The Forty
X-Large = The Growler
XX-Large = The Pony Keg
XXX-Large = The Keg

Industry/Entity Type

It Company

```html
<!DOCTYPE html>
<html lang="en">
<head>
<meta charset="UTF-8">
<title>GROAN Size Chart</title>
<link rel="stylesheet" href="https://fonts.googleapis.com/css2?family=Roboto+Condensed:wght@400;700&display=swap">
<style>
  :root {
    --bg-top: #fdd43e;
    --bg-bottom: #e89d1b;
    --white: #ffffff;
    --ink: #231a0c;
    --diagram-fill: #f3c43a;
    --diagram-line: #b88a22;
  }
  html, body {
    margin: 0;
    padding: 0;
    width: 1200px;
    height: 3000px;
    overflow: hidden;
  }
  .size-chart {
    position: relative;
    width: 1200px;
    height: 3000px;
    background: linear-gradient(180deg, var(--bg-top) 0%, var(--bg-bottom) 100%);
    font-family: "Roboto Condensed", "Arial Narrow", sans-serif;
    overflow: hidden;
  }
  .chart-title {
    position: absolute;
    top: 0;
    left: 0;
    width: 1200px;
    margin: 0;
    padding-top: 66px;
    text-align: center;
    color: var(--white);
    font-weight: 700;
    font-size: 232px;
    line-height: 300px;
    letter-spacing: -5px;
    white-space: nowrap;
  }
  .chart-title span { display: block; }

  .name-key {
    position: absolute;
    top: 640px;
    left: 30px;
    display: grid;
    grid-template-columns: 300px 74px auto;
    color: var(--ink);
    font-size: 60px;
    line-height: 81px;
  }
  .name-key .regular { text-align: right; }
  .name-key .divider {
    grid-row: 1 / span 8;
    grid-column: 2;
    justify-self: center;
    width: 5px;
    background: var(--ink);
    margin: 12px 0 14px;
  }
  .name-key .house { grid-column: 3; }

  .garment-diagram {
    position: absolute;
    left: 795px;
    top: 645px;
    width: 330px;
    height: 615px;
    background: var(--diagram-fill);
    border: 4px solid var(--diagram-line);
    box-sizing: border-box;
  }

  .measure-table {
    position: absolute;
    top: 1455px;
    left: 90px;
    width: 1020px;
    color: var(--white);
    text-align: center;
  }
  .measure-table .row {
    display: grid;
    grid-template-columns: 330px 360px 330px;
  }
  .measure-table .head {
    font-weight: 700;
    font-size: 94px;
    line-height: 100px;
    border-bottom: 6px solid var(--white);
    margin: 0 -30px 0 36px;
    grid-template-columns: 294px 360px 360px;
    letter-spacing: -1px;
  }
  .measure-table .body .row {
    font-size: 78px;
    line-height: 114px;
  }
  .measure-table .body { padding-top: 8px; }

  .site-address {
    position: absolute;
    bottom: 62px;
    left: 0;
    width: 1200px;
    text-align: center;
    color: var(--white);
    font-size: 78px;
    margin: 0;
  }
</style>
</head>
<body>
<main class="size-chart">
  <h1 class="chart-title"><span>GROAN</span><span>SIZE CHART</span></h1>

  <section class="name-key">
    <div class="regular">Regular Size</div><div class="divider"></div><div class="house">GROAN SIZE</div>
    <div class="regular">X-Small</div><div class="house">The Half-Pint</div>
    <div class="regular">Small</div><div class="house">The Pint</div>
    <div class="regular">Medium</div><div class="house">The Bomber</div>
    <div class="regular">Large</div><div class="house">The Forty</div>
    <div class="regular">X-Large</div><div class="house">The Growler</div>
    <div class="regular">XX-Large</div><div class="house">The Pony Keg</div>
    <div class="regular">XXX-Large</div><div class="house">The Keg</div>
  </section>

  <div class="garment-diagram" role="img" aria-label="Technical drawing of a cycling jersey and shorts with measurement lines A, B and C"></div>

  <section class="measure-table">
    <div class="row head"><div>Men’s</div><div>Chest</div><div>Women’s</div></div>
    <div class="body">
      <div class="row"><div>-</div><div>34</div><div>XS</div></div>
      <div class="row"><div>-</div><div>36</div><div>S</div></div>
      <div class="row"><div>-</div><div>38</div><div>M</div></div>
      <div class="row"><div>S</div><div>40</div><div>L</div></div>
      <div class="row"><div>M</div><div>42.5</div><div>XL</div></div>
      <div class="row"><div>L</div><div>45</div><div>XXL</div></div>
      <div class="row"><div>XL</div><div>47.5</div><div>-</div></div>
      <div class="row"><div>XXL</div><div>50</div><div>-</div></div>
      <div class="row"><div>XXXL</div><div>52.5</div><div>-</div></div>
    </div>
  </section>

  <p class="site-address">www.groankitvale.com</p>
</main>
</body>
</html>
```